The Willow Barn Holiday Cottages

1 bedroom & 2 bedroom holiday cottagesRural SettingBeautiful viewsPeaceful and tranquil location yet only 20 minutes from Durham city. 30 minutes from Newcastle.Newly built, fully equipped Welcome pack, toiletries, bed linen and towels all included.ideal for walkers and cyclists alike. Within walking distance of The award winning Farm Shop. Local pub also within walking distance.

Target Market(s)

Couples and families with children. Dogs welcome. Stabling available for horses.

Font styles to use
Decorative

Requirements
Must have
• My contact details on the reverse side of the postcard.
Nice to have
• A holiday style description on the reverse side of the postcard.

```html
<!DOCTYPE html>
<html lang="en">
<head>
<meta charset="utf-8">
<title>The Willow Barn Holiday Cottages – Postcard</title>
<link rel="stylesheet" href="https://fonts.googleapis.com/css2?family=Playfair+Display:ital,wght@1,600;1,700&family=Open+Sans:wght@400;600&display=swap">
<style>
  :root {
    --backdrop: #d9d7d3;
    --paper: #eceae6;
    --paper-edge: #c9c6c0;
    --frame-red: #b3242a;
    --frame-white: #ffffff;
    --ink-dark: #2a2a2a;
    --ink-blue: #2f7fc1;
    --rule: #8a8a8a;
    --photo-house-a: #c9a24a;
    --photo-house-b: #7c8a5a;
    --photo-room-a: #d9d4ca;
    --photo-room-b: #8f8a82;
    --photo-lounge-a: #e3ddd2;
    --photo-lounge-b: #9c9184;
    --photo-view-a: #9fb6c9;
    --photo-view-b: #6f7f4a;
  }
  * { box-sizing: border-box; margin: 0; padding: 0; }
  html, body { width: 900px; height: 1200px; overflow: hidden; }
  body { background: var(--backdrop); font-family: "Open Sans", sans-serif; position: relative; }

  .postcard {
    position: absolute; left: 30px; width: 840px; height: 530px;
    background: var(--paper);
    border: 1px solid var(--paper-edge);
    box-shadow: 0 4px 14px rgba(0,0,0,.18);
  }
  .postcard--front { top: 40px; }
  .postcard--back { top: 630px; }

  .photo {
    position: absolute;
    border: 4px solid var(--frame-red);
    outline: 4px solid var(--frame-white);
    box-shadow: 2px 4px 10px rgba(0,0,0,.3);
  }
  .photo--house { left: 42px; top: 22px; width: 220px; height: 150px; transform: rotate(-9deg);
    background: linear-gradient(160deg, var(--photo-view-a) 0%, var(--photo-house-a) 45%, var(--photo-house-b) 100%); }
  .photo--bedroom { left: 52px; top: 190px; width: 215px; height: 150px;
    background: linear-gradient(170deg, var(--photo-room-a), var(--photo-room-b)); }
  .photo--lounge { left: 250px; top: 110px; width: 250px; height: 190px;
    background: linear-gradient(170deg, var(--photo-lounge-a), var(--photo-lounge-b)); }

  .front-text { position: absolute; right: 40px; top: 340px; width: 420px; text-align: center; }
  .front-text__title { font-family: "Playfair Display", serif; font-style: italic; font-weight: 700;
    font-size: 26px; color: var(--ink-dark); margin-bottom: 8px; }
  .front-text__distance { font-weight: 600; font-size: 17px; color: var(--ink-blue); line-height: 1.35; }
  .front-text__address { font-size: 16px; color: var(--ink-dark); line-height: 1.35; margin-top: 8px; }

  .tab {
    position: absolute; left: 14px; top: 20px; width: 250px; height: 40px;
    border: 2px solid var(--frame-red); border-left: none; border-top: none;
    border-bottom-right-radius: 8px;
    background: var(--paper);
    font-family: "Playfair Display", serif; font-style: italic; font-weight: 600;
    font-size: 19px; color: var(--ink-dark); padding: 6px 14px;
  }
  .features { position: absolute; left: 36px; top: 86px; width: 360px; list-style: none; }
  .features li { font-size: 14px; color: var(--ink-blue); line-height: 1.4; padding-left: 12px; position: relative; }
  .features li::before { content: "•"; position: absolute; left: 0; }
  .features li.gap { margin-top: 12px; }

  .contact { position: absolute; left: 36px; top: 282px; width: 360px;
    font-size: 13px; line-height: 1.4; color: var(--ink-dark); }
  .contact__name { font-family: "Playfair Display", serif; font-style: italic; font-weight: 600; font-size: 15px; }

  .divider { position: absolute; left: 420px; top: 70px; width: 1px; height: 400px; background: var(--rule); }
  .stamp-box { position: absolute; right: 50px; top: 40px; width: 110px; height: 130px; border: 2px solid var(--ink-dark); }
  .address-lines { position: absolute; left: 470px; top: 250px; width: 320px; }
  .address-lines span { display: block; height: 1px; background: var(--rule); margin-bottom: 44px; }

  .photo--view { left: 34px; top: 370px; width: 190px; height: 120px; transform: rotate(-4deg);
    background: linear-gradient(180deg, var(--photo-view-a) 0%, var(--photo-view-a) 40%, var(--photo-view-b) 100%); }
  .photo--cottage { left: 220px; top: 360px; width: 180px; height: 130px; transform: rotate(3deg);
    background: linear-gradient(170deg, var(--photo-house-a), var(--photo-house-b)); }
</style>
</head>
<body>
  <section class="postcard postcard--front">
    <div class="photo photo--house" role="img" aria-label="Photo of the cottage exterior"></div>
    <div class="photo photo--bedroom" role="img" aria-label="Photo of a cottage bedroom"></div>
    <div class="photo photo--lounge" role="img" aria-label="Photo of the cottage living room"></div>
    <div class="front-text">
      <h1 class="front-text__title">The Willow Barn Holiday Cottages</h1>
      <p class="front-text__distance">only 20 minutes from Durham city.<br>30 minutes from Newcastle.</p>
      <p class="front-text__address">123 Your Street<br>Anytown, Your State</p>
    </div>
  </section>

  <section class="postcard postcard--back">
    <h2 class="tab">Holiday style description</h2>
    <ul class="features">
      <li>1 bedroom &amp; 2 bedroom holiday cottages</li>
      <li>Rural Setting Beautiful views Peaceful</li>
      <li>Newly built, fully equipped Welcome pack, toiletries, bed linen and towels all included</li>
      <li>Ideal for walkers and cyclists alike</li>
      <li class="gap">Within walking distance of The award winning Farm Shop</li>
      <li>Local pub also within walking distance</li>
    </ul>
    <address class="contact">
      <span class="contact__name">The Willow Barn Holiday Cottages</span><br>
      123 Your Street, Anytown, Your State
    </address>
    <div class="divider"></div>
    <div class="stamp-box"></div>
    <div class="address-lines"><span></span><span></span><span></span><span></span></div>
    <div class="photo photo--view" role="img" aria-label="Photo of the rural countryside view"></div>
    <div class="photo photo--cottage" role="img" aria-label="Photo of the cottages and courtyard"></div>
  </section>
</body>
</html>
```